"Brindle Oak Accupuncture" needs a Promotional Card - A6 size

Requirements
Must have
• Bright colours, pictures of happy people, acupuncture-related pictures.

```html
<!DOCTYPE html>
<html lang="en">
<head>
<meta charset="utf-8">
<title>Brindle Oak Accupuncture – A6 Promotional Card</title>
<link href="https://fonts.googleapis.com/css2?family=Source+Sans+3:wght@400;600;700&display=swap" rel="stylesheet">
<style>
  :root {
    --red: #e23b26;
    --red-deep: #c9301d;
    --slate: #2f3e46;
    --ink: #1f1f1f;
    --white: #ffffff;
    --gold: #f0a92a;
    --stage-light: #bdbdbd;
    --stage-dark: #5e5e5e;
  }
  * { box-sizing: border-box; margin: 0; padding: 0; }
  html, body { width: 1200px; height: 1200px; overflow: hidden; }
  body {
    font-family: "Source Sans 3", "Source Sans Pro", sans-serif;
    background: radial-gradient(ellipse at 50% 30%, var(--stage-light) 0%, #9a9a9a 45%, var(--stage-dark) 100%);
    position: relative;
    color: var(--ink);
  }
  .board-title {
    position: absolute; top: 128px; left: 0; width: 1200px;
    text-align: center; font-weight: 700; font-size: 34px; color: #8c8c8c;
  }
  .card {
    position: absolute; top: 198px; width: 570px; height: 804px;
    background: var(--white); overflow: hidden;
    box-shadow: 0 6px 16px rgba(0,0,0,.45);
  }
  .card--front { left: 22px; }
  .card--back { left: 609px; }
  .abs { position: absolute; }
  .art { position: absolute; inset: 0; width: 100%; height: 100%; }

  /* front */
  .brand {
    position: absolute; top: 80px; left: 330px; width: 220px; text-align: center;
  }
  .brand__dot { width: 26px; height: 26px; border-radius: 50%; background: var(--gold); margin: 0 auto 8px; }
  .brand__name { color: var(--red); font-weight: 700; font-size: 27px; line-height: 25px; }
  .subtitle {
    position: absolute; top: 166px; left: 198px; width: 340px;
    color: var(--white); font-size: 35px; font-weight: 400; white-space: nowrap;
  }
  .section-head {
    position: absolute; display: flex; align-items: center; gap: 14px;
    font-weight: 700; font-size: 19.5px; letter-spacing: .3px; color: var(--ink);
  }
  .section-head__mark { width: 22px; height: 22px; border-radius: 50%; background: var(--gold); margin-left: 15px; margin-right: 8px; }
  .body-copy { position: absolute; font-size: 16px; line-height: 20.8px; color: var(--ink); }
  .quote-band {
    position: absolute; left: 0; top: 676px; width: 570px; height: 92px;
    background: rgba(40,30,28,.9);
  }
  .quote-band__icon { position: absolute; left: 36px; top: 22px; }
  .quote-band__lead { position: absolute; left: 95px; top: 18px; color: var(--white); font-size: 18px; }
  .quote-band__lead b { font-weight: 700; }
  .quote-band__number { position: absolute; left: 95px; top: 38px; color: var(--white); font-weight: 700; font-size: 37px; }
  .quote-band__dot { position: absolute; right: 44px; top: 28px; width: 36px; height: 36px; border-radius: 50%; background: var(--gold); }

  /* back */
  .hours { position: absolute; left: 54px; top: 438px; font-size: 16px; line-height: 21px; border-collapse: collapse; }
  .hours td { padding: 0 13px 0 0; }
  .address { position: absolute; left: 54px; top: 553px; font-size: 18px; line-height: 23px; }
  .social { position: absolute; left: 276px; top: 555px; display: flex; align-items: center; gap: 10px; font-size: 17px; font-weight: 600; color: var(--slate); }
  .social__dot { width: 34px; height: 34px; border-radius: 50%; background: var(--red); }
  .contact { position: absolute; left: 257px; top: 690px; list-style: none; color: var(--white); font-size: 18px; }
  .contact li { display: flex; align-items: center; gap: 9px; height: 30.5px; }
</style>
</head>
<body>
  <div class="board-title">A6 Flyer</div>

  <!-- Front of card -->
  <section class="card card--front">
    <svg class="art" viewBox="0 0 570 804" aria-hidden="false">
      <defs>
        <linearGradient id="treatmentTone" x1="0" y1="0" x2="1" y2="1">
          <stop offset="0" stop-color="#c79a6c"/>
          <stop offset=".55" stop-color="#e8cdb0"/>
          <stop offset="1" stop-color="#f6efe8"/>
        </linearGradient>
        <linearGradient id="handsTone" x1="0" y1="0" x2="0" y2="1">
          <stop offset="0" stop-color="#ffffff"/>
          <stop offset="1" stop-color="#f1ddd6"/>
        </linearGradient>
        <linearGradient id="parkTone" x1="0" y1="0" x2="0" y2="1">
          <stop offset="0" stop-color="#cfdcb8"/>
          <stop offset=".6" stop-color="#a9b98a"/>
          <stop offset="1" stop-color="#6f9a4a"/>
        </linearGradient>
      </defs>
      <rect x="0" y="360" width="570" height="444" fill="url(#handsTone)" role="img" aria-label="Faded photo of therapist's hands during treatment"/>
      <path d="M0 0 H570 V300 Q430 255 280 265 Q120 272 0 300 Z" fill="url(#treatmentTone)" role="img" aria-label="Photo of acupuncture needles placed on a patient's shoulder"/>
      <path d="M0 290 Q150 240 290 272 Q170 258 0 332 Z" fill="var(--red)"/>
      <circle cx="426" cy="418" r="182" fill="var(--red)"/>
      <circle cx="440" cy="410" r="162" fill="url(#parkTone)" role="img" aria-label="Photo of a happy family playing together on the grass"/>
    </svg>

    <div class="brand">
      <div class="brand__dot"></div>
      <div class="brand__name">Brindle Oak<br>Accupuncture</div>
    </div>
    <div class="subtitle">Additional Title Here</div>

    <h2 class="section-head" style="left:14px; top:312px;"><span class="section-head__mark"></span>ABOUT US</h2>
    <p class="body-copy" style="left:47px; top:350px; width:210px;">Lorem ipsum dolor sit amet, consectetur adipiscing elit. Sed tempus orci turpis, sit amet ultricies tellus aliquet in. Nullam at suscipit nisl, vel interdum est. Vestibulum et placerat ipsum, vitae.</p>

    <h2 class="section-head" style="left:14px; top:555px;"><span class="section-head__mark"></span>OUR MISSION</h2>
    <p class="body-copy" style="left:47px; top:591px; width:320px;">Lorem ipsum dolor sit amet, consectetur adipiscing elit. Sed tempus orci turpis, sit amet ultricies tellus aliquet in.</p>

    <div class="quote-band">
      <svg class="quote-band__icon" width="48" height="52" viewBox="0 0 24 24" aria-hidden="true">
        <path fill="#fff" d="M6.6 10.8a15.2 15.2 0 0 0 6.6 6.6l2.2-2.2a1 1 0 0 1 1-.25 11.4 11.4 0 0 0 3.6.57 1 1 0 0 1 1 1V20a1 1 0 0 1-1 1A17 17 0 0 1 3 4a1 1 0 0 1 1-1h3.5a1 1 0 0 1 1 1c0 1.25.2 2.45.57 3.57a1 1 0 0 1-.25 1z"/>
      </svg>
      <div class="quote-band__lead"><b>FREE QUOTE</b> CALL OR TEXT</div>
      <div class="quote-band__number">888-888-8888</div>
      <div class="quote-band__dot"></div>
    </div>
  </section>

  <!-- Back of card -->
  <section class="card card--back">
    <svg class="art" viewBox="0 0 570 804">
      <defs>
        <linearGradient id="patientTone" x1="0" y1="0" x2="1" y2="1">
          <stop offset="0" stop-color="#f2f2f0"/>
          <stop offset=".6" stop-color="#ddd3de"/>
          <stop offset="1" stop-color="#c9bccb"/>
        </linearGradient>
        <linearGradient id="stoneTone" x1="0" y1="0" x2="1" y2="0">
          <stop offset="0" stop-color="#e9c2a8"/>
          <stop offset="1" stop-color="#b8705a"/>
        </linearGradient>
      </defs>
      <path d="M0 0 H236 Q270 90 268 210 Q260 330 200 360 Q100 385 0 340 Z" fill="url(#patientTone)" role="img" aria-label="Photo of an older woman holding her aching back"/>
      <path d="M240 0 H570 V160 Q440 162 330 198 Q300 80 240 0 Z" fill="url(#stoneTone)" role="img" aria-label="Photo of a hot stone massage on a patient's back"/>
      <path d="M330 198 Q440 162 570 160 V172 Q440 172 336 212 Z" fill="var(--red)"/>
      <circle cx="249" cy="266" r="104" fill="#fff"/>
      <circle cx="249" cy="266" r="94" fill="#f0d2c3" role="img" aria-label="Photo of fingers pressing an acupressure point on a wrist"/>
      <path d="M0 663 Q180 620 330 630 Q470 640 570 660 V804 H0 Z" fill="var(--slate)"/>
      <path d="M0 663 Q60 655 120 660 V700 Q60 692 0 700 Z" fill="var(--red)"/>
      <path d="M190 640 Q400 600 570 650 V666 Q400 620 200 660 Z" fill="var(--red)"/>
      <circle cx="127" cy="695" r="82" fill="#fff"/>
      <circle cx="127" cy="695" r="73" fill="#d9cfc8" role="img" aria-label="Portrait photo of the practitioner"/>
    </svg>

    <p class="body-copy" style="left:366px; top:214px; width:190px; font-size:14.2px; line-height:18.4px;">Lorem ipsum dolor sit amet, consectetur adipiscing elit. Sed tempus orci turpis, sit amet ultricies tellus aliquet in.</p>
    <p class="body-copy" style="left:366px; top:324px; width:190px; font-size:14.2px; line-height:18.4px;">Nullam at suscipit nisl, vel interdum est. Vestibulum et placerat ipsum, vitae. Nullam at suscipit nisl, vel interdum est. Vestibulum et placerat ipsum, vitae. Sed tempus orci turpis, sit amet ultricies tellus aliquet in.</p>

    <h2 class="section-head" style="left:13px; top:401px;"><span class="section-head__mark"></span>HOURS</h2>
    <table class="hours">
      <tr><td>Monday to Friday</td><td>9:00 AM – 7:00 PM</td></tr>
      <tr><td>Saturday</td><td>9:00 AM – 3:00 PM</td></tr>
    </table>

    <h2 class="section-head" style="left:13px; top:513px;"><span class="section-head__mark"></span>LOCATION</h2>
    <p class="address">Unit, Street, City<br>State, Zip Code</p>

    <h2 class="section-head" style="left:215px; top:513px;"><span class="section-head__mark"></span>FIND US ON</h2>
    <div class="social"><span class="social__dot"></span>@brindleoak</div>

    <ul class="contact">
      <li>
        <svg width="18" height="18" viewBox="0 0 24 24" aria-hidden="true"><path fill="none" stroke="#fff" stroke-width="1.6" d="M6.6 10.8a15.2 15.2 0 0 0 6.6 6.6l2.2-2.2a1 1 0 0 1 1-.25 11.4 11.4 0 0 0 3.6.57 1 1 0 0 1 1 1V20a1 1 0 0 1-1 1A17 17 0 0 1 3 4a1 1 0 0 1 1-1h3.5a1 1 0 0 1 1 1c0 1.25.2 2.45.57 3.57a1 1 0 0 1-.25 1z"/></svg>
        888-888-8888
      </li>
      <li>
        <svg width="18" height="18" viewBox="0 0 24 24" aria-hidden="true"><rect x="2" y="5" width="20" height="14" fill="none" stroke="#fff" stroke-width="1.8"/><path d="M2 5l10 8 10-8" fill="none" stroke="#fff" stroke-width="1.8"/></svg>
        name@email.com
      </li>
      <li>
        <svg width="18" height="18" viewBox="0 0 24 24" aria-hidden="true"><path d="M3 11l9-8 9 8M5 9v12h14V9M10 21v-6h4v6" fill="none" stroke="#fff" stroke-width="1.8"/></svg>
        domain.com
      </li>
    </ul>
  </section>
</body>
</html>
```